Homecare Information Flyer

We require a brochure/ leaflet to be created which would provide healthcare information to our staff and patients on the topic of- Pressure Ulcers. The document would ideally be 3 fold. It should include our Logo/ Company Information (Marlowe Staffing).

I have attached-
- Logo
- Text/ Visual images to be included.

Industry/Entity Type

Healthcare

```html
<!DOCTYPE html>
<html lang="en">
<head>
<meta charset="utf-8">
<title>Pressure Area Care – Guide for patients</title>
<link href="https://fonts.googleapis.com/css2?family=Oswald:wght@400;500&family=Open+Sans:wght@400;600;700&display=swap" rel="stylesheet">
<style>
  :root{
    --green:#7dc142;
    --green-dark:#5fa22c;
    --ink:#3b3b3b;
    --muted:#555;
    --paper:#ffffff;
    --edge:#3a3a3a;
    --backdrop:#ececec;
    --fold:#e6e6e6;
    --pink:#f3dbe6;
  }
  *{box-sizing:border-box;margin:0;padding:0}
  html,body{width:1200px;height:874px;overflow:hidden}
  body{background:var(--backdrop);font-family:"Open Sans",Arial,sans-serif;color:var(--ink);position:relative}

  .spread{position:absolute;width:630px;height:420px;background:var(--paper);display:flex;box-shadow:0 4px 14px rgba(0,0,0,.18)}
  .spread::before{content:"";position:absolute;left:0;top:0;right:0;height:6px;background:var(--edge);z-index:3}
  .spread--inside{left:555px;top:14px}
  .spread--outside{left:15px;top:444px}

  .panel{position:relative;width:210px;height:100%;padding:16px 10px 10px 0;overflow:hidden}
  .panel + .panel{border-left:1px solid var(--fold)}

  .tag{display:inline-block;background:var(--green);color:#fff;font-family:"Oswald",Arial,sans-serif;font-weight:400;font-size:9px;line-height:1;padding:4px 10px 4px 10px;margin:7px 0 3px}
  .copy{font-size:6.4px;line-height:1.42;padding-left:10px;color:var(--muted)}
  .copy strong{font-weight:700;color:var(--ink)}

  /* inside right panel */
  .pose{font-family:"Oswald",Arial,sans-serif;font-size:6.5px;color:var(--green);font-style:normal;padding-left:14px;margin:8px 0 3px}
  .pose::before{content:"→ ";}
  .figure{margin:0 0 0 10px;width:190px;background:linear-gradient(#f7f7f7,#ebebeb);border:1px solid #ddd}
  .figure--back{height:44px}
  .figure--side{height:48px}
  .figure--chair{height:92px;background:linear-gradient(135deg,#f8e7ee,var(--pink));border-radius:4px}

  /* outside */
  .brand{display:flex;align-items:center;justify-content:center;gap:5px;font-family:"Open Sans",Arial,sans-serif;font-weight:700;font-size:10px;color:var(--green-dark)}
  .brand-dot{width:12px;height:12px;border-radius:50%;background:var(--green)}
  .panel--contact .brand{margin-top:18px}
  .contact-title{margin:70px 16px 0;border-top:1px solid var(--green);border-bottom:1px solid var(--green);padding:6px 0;text-align:center;font-family:"Oswald",Arial,sans-serif;font-size:15px;color:var(--green);font-weight:400}
  .contact-name{text-align:center;font-family:"Oswald",Arial,sans-serif;font-size:10px;font-weight:500;margin-top:12px}
  .contact-role{text-align:center;font-family:"Oswald",Arial,sans-serif;font-size:7.5px;font-weight:400;color:var(--muted);margin-top:2px}
  .contact-links{position:absolute;left:0;right:0;bottom:20px;text-align:center;color:#fff;font-size:6.3px;line-height:2;z-index:2}

  .panel--cover .brand{margin-top:18px;position:relative;z-index:2}
  .cover-photo{position:absolute;left:16px;right:0;top:48px;height:270px;background:linear-gradient(160deg,#f4f6f3 0%,#dfe9dc 55%,#b9d9b8 100%)}
  .cover-title{position:absolute;left:14px;right:14px;bottom:22px;z-index:2;color:#fff;text-align:center;font-family:"Oswald",Arial,sans-serif}
  .cover-title h1{font-size:16px;font-weight:400;border-top:1px solid rgba(255,255,255,.7);border-bottom:1px solid rgba(255,255,255,.7);padding:4px 0}
  .cover-title p{font-size:9.5px;margin-top:8px;font-weight:400}

  .bands{position:absolute;left:210px;top:0;width:420px;height:420px;z-index:1}
</style>
</head>
<body>

<!-- Inside spread -->
<section class="spread spread--inside" aria-label="Leaflet inside">
  <div class="panel">
    <span class="tag">What is a Pressure Ulcer?</span>
    <p class="copy">A pressure ulcer is an area of damage to the skin and underlying tissue.<br>They are sometimes known as pressure sores or bed sores.</p>
    <span class="tag">What causes a Pressure Ulcer?</span>
    <p class="copy">Pressure ulcers are caused by poor circulation to tissues due to a combination of the following factors:</p>
    <span class="tag">Pressure</span>
    <p class="copy">Body weight and some equipment (e.g. anti-thrombosis stockings) can squash the skin and other tissues where parts are under pressure. This reduces the blood supply to the area and can lead to tissue damage.</p>
    <span class="tag">Shearing</span>
    <p class="copy">Sliding or slumping down the bed/chair can damage the skin and deeper layers of tissue.</p>
    <span class="tag">Friction</span>
    <p class="copy">Rubbing of the skin against bedding, clothing or equipment can damage the fragile surface layer, especially when moving or being moved.</p>
  </div>
  <div class="panel">
    <span class="tag">Moist Skin</span>
    <p class="copy">You may be at increased risk if your skin is too damp, due to incontinence, sweat or a weeping wound. It is important that your skin is kept clean and healthy.</p>
    <span class="tag">Lack of Sensitivity to Pain of Discomfort</span>
    <p class="copy">Conditions such as Diabetes Stroke, Nerve, Muscle Disorders, etc. reduce the normal sensations that usually prompt you, or enable you to move. Some treatments (e.g. Epidural pain relief, medications, and operations) reduce your sensitivity to pain or discomfort so that you are not aware of the need to move.</p>
    <span class="tag">Previous Tissue Damage</span>
    <p class="copy">Scar tissue will have lost some of its previous strength and is more prone to breakdown.</p>
    <span class="tag">Inadequate Diet of Fluid Intake</span>
    <p class="copy">Lack of fluid may dehydrate your tissues. Weight gain or loss can change fat distribution over bony points and leave skin more fragile.</p>
    <p class="copy" style="margin-top:5px">If you are at risk of developing Pressure Ulcers, a member of your healthcare team will examine/assess you and your skin regularly. This will help to identify if you need special equipment or other forms of care, and plan care to meet your individual needs.</p>
    <span class="tag">How will I know if I have a Pressure Ulcer?</span>
    <p class="copy"><strong>Look out for these early signs:</strong><br>Skin that is red or darker than usual, patches that feel hot, spongy or hard, pain or itching.</p>
  </div>
  <div class="panel">
    <p class="copy" style="margin-top:6px">Without appropriate intervention the damage may worsen, developing into hard black tissue or an open wound.</p>
    <span class="tag">Common Locations of Pressure Ulcers</span>
    <p class="pose">Laying on your back</p>
    <div class="figure figure--back" role="img" aria-label="Outline drawing of a person lying on their back with pressure points marked at the back of head, shoulder blade, elbow, coccyx and heel"></div>
    <p class="pose">Laying on your side</p>
    <div class="figure figure--side" role="img" aria-label="Outline drawing of a person lying on their side with pressure points marked at the ear, shoulder, elbow, hip, thigh, lower leg and heel"></div>
    <p class="pose">Sitting in a chair</p>
    <div class="figure figure--chair" role="img" aria-label="Illustration of a person seated in a wheelchair with pressure points marked at the scapula, elbow, sacrum, ischium, heel and ball of foot"></div>
  </div>
</section>

<!-- Outside spread -->
<section class="spread spread--outside" aria-label="Leaflet outside">
  <div class="panel">
    <span class="tag">What can I do to Avoid Pressure Ulcers?</span>
    <p class="copy">There are several ways you can reduce the risk of pressure ulcers.</p>
    <span class="tag">Keep Moving</span>
    <p class="copy">Changing your position regularly helps keep blood flowing. If you have reduced movement the Health Care team looking after you will assist you with regular turns in addition to providing specialist mattresses, cushions, boots etc.</p>
    <span class="tag">Look for signs of Damage</span>
    <p class="copy">Check your skin for pressure damage at least once a day. Look for skin that doesn't go back to its normal colour after you have taken the weight off it. Do not continue to lie on skin that is redder of darker than usual. Also watch out for blisters, dry patches or breaks in the skin.</p>
    <span class="tag">Protect your Skin</span>
    <p class="copy">Wash your skin using warm water of PH Neutral skin cleansers. Do not use heavily perfumed soap or talcum powder as these can soak up the skins natural oils leading to vulnerable dry areas. If you suffer from incontinence please inform your health care team as they can assess the best way to deal with the problems. Rubbing/massaging skin is bad for it.</p>
    <span class="tag">Eat a Well-balanced Diet</span>
    <p class="copy">Make sure you eat a healthy balanced diet and drink plenty of fluids. Extra protein may help.</p>
    <span class="tag">What should I do if I suspect a pressure ulcer?</span>
    <p class="copy">Tell your Doctor or Nurse as soon as possible and follow the advice they give you</p>
  </div>

  <div class="panel panel--contact">
    <div class="brand"><span class="brand-dot"></span>Marlowe Staffing</div>
    <h2 class="contact-title">CONTACT US TODAY</h2>
    <p class="contact-name">Rowena Hale</p>
    <p class="contact-role">- Clinical Nurse Specialist -</p>
    <p class="contact-links">rowena.hale@marlowestaffing.co.uk<br>www.marlowestaffing.co.uk</p>
  </div>

  <div class="panel panel--cover">
    <div class="brand"><span class="brand-dot"></span>Marlowe Staffing</div>
    <div class="cover-photo" role="img" aria-label="Photograph of a smiling nurse in green scrubs with a stethoscope, writing on a clipboard"></div>
    <div class="cover-title">
      <h1>PRESSURE AREA CARE</h1>
      <p>Guide for patients</p>
    </div>
  </div>

  <svg class="bands" viewBox="0 0 420 420" aria-hidden="true">
    <polygon points="0,332 210,340 210,420 0,420" fill="var(--green)"/>
    <polygon points="210,345 420,300 420,420 210,420" fill="var(--green)"/>
  </svg>
</section>

</body>
</html>
```